Retirement Plan Advisor Bio

See the attached document and photo for content. I would like someone to design this one page flyer using my logo. This logo was designed by a designer with sketch hive. I am looking for a professional looking document. I want to he color scheme to be primarily white and gold.

Target Market(s)

Employers who offer a retirement plan

Requirements
Should not have
• The designs that I have received look more like resumes. I am interested in advertising my Retirement plan services. If anyone can change their submissions and change it to an ad for retirement plan services instead of a Bio or resume, I would prefer that.

```html
<!DOCTYPE html>
<html lang="en">
<head>
<meta charset="utf-8">
<title>Claire M Adler – Retirement Plan Advisor</title>
<link href="https://fonts.googleapis.com/css2?family=Fira+Sans:ital,wght@0,400;0,600;1,400;1,600&display=swap" rel="stylesheet">
<style>
  :root {
    --gold: #c1a36a;
    --gold-deep: #a98a4e;
    --ink: #262320;
    --ink-brown: #33291b;
    --white: #ffffff;
  }
  * { margin: 0; padding: 0; box-sizing: border-box; }
  html, body { width: 927px; height: 1200px; overflow: hidden; background: var(--white); }
  body { font-family: "Fira Sans", Arial, sans-serif; color: var(--ink); }
  .flyer { position: relative; width: 927px; height: 1200px; overflow: hidden; background: var(--white); }

  .hero-band { position: absolute; left: 0; top: 244px; width: 927px; height: 322px; background: var(--gold); }

  .portrait-frame {
    position: absolute; left: 24px; top: 15px; width: 305px; height: 414px;
    background: var(--white); box-shadow: 2px 3px 6px rgba(0,0,0,0.25);
  }
  .portrait {
    position: absolute; left: 9px; top: 7px; width: 288px; height: 399px;
    background: linear-gradient(180deg, #7d8fb0 0%, #9aa6be 35%, #c9a98a 60%, #2a2a2c 80%, #1d1d1f 100%);
  }

  .brand {
    position: absolute; left: 352px; top: 118px;
    display: flex; align-items: center; gap: 14px;
  }
  .brand-mark { width: 34px; height: 34px; background: var(--gold-deep); }
  .brand-name { font-size: 44px; font-weight: 400; color: var(--gold-deep); letter-spacing: 0.5px; line-height: 1; }

  .advisor { position: absolute; left: 356px; top: 256px; color: var(--ink); }
  .advisor-name { font-size: 19px; font-weight: 600; line-height: 24px; }
  .advisor-role { font-size: 17px; line-height: 22px; }
  .advisor-phone { font-size: 21px; font-weight: 600; line-height: 26px; margin-top: 15px; }
  .advisor-email { font-size: 17px; line-height: 22px; margin-top: 2px; }
  .advisor-web { font-size: 18px; font-weight: 600; font-style: italic; line-height: 24px; }

  .mission {
    position: absolute; left: 20px; top: 451px; width: 887px;
    text-align: center; color: var(--white);
    font-size: 24px; font-weight: 600; font-style: italic; line-height: 30px;
  }

  .section { position: absolute; left: 46px; width: 840px; }
  .section h2 { font-size: 27px; font-weight: 600; font-style: italic; line-height: 34px; }
  .section ul { list-style: none; margin-top: 6px; }
  .section li { font-size: 18.5px; line-height: 24.5px; }
  .section li::before { content: "• "; }
  .specialties { top: 622px; }
  .qualifications { top: 785px; }
  .education { top: 974px; }

  .disclosure { position: absolute; left: 49px; top: 1091px; width: 820px; font-size: 13.5px; line-height: 18px; }

  .footer-band {
    position: absolute; left: 0; top: 1143px; width: 927px; height: 57px;
    background: var(--gold); color: var(--ink-brown);
    font-size: 24px; font-weight: 600; text-align: center; line-height: 57px;
  }
</style>
</head>
<body>
<main class="flyer">
  <div class="hero-band"></div>

  <div class="portrait-frame">
    <div class="portrait" role="img" aria-label="Portrait photograph of the advisor in a dark blazer against a soft blue backdrop"></div>
  </div>

  <div class="brand">
    <span class="brand-mark"></span>
    <span class="brand-name">Keystone Financial, LLC</span>
  </div>

  <section class="advisor">
    <p class="advisor-name">Claire M Adler CFP®AIF®</p>
    <p class="advisor-role">Meridian Securities Advisor</p>
    <p class="advisor-phone">(555)210.4837</p>
    <p class="advisor-email">claire.adler@meridiansec.com</p>
    <p class="advisor-web">Www.claireadler.com</p>
  </section>

  <p class="mission">I strive to improve retirement outcomes for my plan sponsor clients and their employees through careful retirement plan design assistance, strategic and targeted communication and education, as well as continual monitoring of results.</p>

  <section class="section specialties">
    <h2>Professional Specialties</h2>
    <ul>
      <li>Over 18 years of experience in the retirement plan industry</li>
      <li>Focused on helping plan sponsors reduce administrative burdens and fiduciary risk</li>
      <li>Dedicated to helping employees work toward a positive retirement outcome through careful analysis of their savings rate , investment strategy and overall financial wellness</li>
    </ul>
  </section>

  <section class="section qualifications">
    <h2>Qualifications</h2>
    <ul>
      <li>Certified Financial Planner®</li>
      <li>Accredited Investment Fiduciary®</li>
      <li>Investment Advisor Representative</li>
      <li>Series 7, 63, and 65 Securities licenses with Meridian Securities</li>
      <li>Holds Life and Health Insurance licenses from Illinois</li>
    </ul>
  </section>

  <section class="section education">
    <h2>Education</h2>
    <ul>
      <li>BS Westbrook University, 1987</li>
    </ul>
  </section>

  <p class="disclosure">*Securities and Investment Advisory Services offered through Meridian Securities Holdings, Inc, a Registered Broker/Dealer and Investment Advisor, member NSRA/SIPF</p>

  <footer class="footer-band">2400 Larkfield Road • Fairview, IL 60999 • (555)210.4837</footer>
</main>
</body>
</html>
```